Landing Page for Bathroom Remodeling Webpage - Desktop and Mobile

I am looking for some help designing the "above the fold" area for my bathroom remodeling service page. Looking for something a little different than the rest. Typically remodeling companies just put a nice picture of a bathroom remodel but I would like to do something a little different / more creative. Below is a link to the current wireframe we are working on.
Current website is located at plumvantaridge.com
Again the biggest thing I am looking for is a design for the very top section but would love help on the rest of the page as well. You will see by viewing the link below the type of information we are looking to include on the page:
PLEASE DO INCLUDE WHAT THE MOBILE VERSION WOULD LOOK LIKE AS WELL.
Wireframe:
https://boards.quillmerra.com/view/3f8a1b2c-90de-4e7a-b5c1-aa62d09e1f35-418k/
There are also comments in the link above you can read as well.
We like the idea of something interactive such as this...
https://pixorvale.com/shots/5192746-Glenhart-Scooter-Store-Animation
Attached is also the logo we want to use going forward
Target Market(s)
Residential homeowners, 30 years old+ with professional careers
Number of Pages Required
1 page
Look and feel
Each slider illustrates characteristics of the customer's brand and the style your logo design should communicate.

```html
<!DOCTYPE html>
<html lang="en">
<head>
<meta charset="utf-8">
<title>Plumvanta – Bathroom Remodeling</title>
<link href="https://fonts.googleapis.com/css2?family=Poppins:wght@400;500;600;700&display=swap" rel="stylesheet">
<style>
:root{
  --red:#d8231f;
  --navy:#0d2556;
  --dark:#1f2024;
  --ink:#1d1d24;
  --grey:#6d6f76;
  --light:#f4f4f5;
  --line:#e3e3e6;
  --white:#ffffff;
}
*{box-sizing:border-box;margin:0;padding:0}
html,body{width:1200px;height:3788px;overflow:hidden}
body{background:#ededee;font-family:'Poppins',sans-serif;color:var(--ink)}
.page{position:absolute;left:290px;top:31px;width:620px;height:3725px;background:var(--white);box-shadow:0 6px 30px rgba(0,0,0,.12);overflow:hidden}
section,header,footer{position:relative;width:620px}
.abs{position:absolute}
.placeholder{position:absolute}

/* header */
.site-header{height:44px;background:var(--white)}
.nav{position:absolute;top:17px;display:flex;gap:10px;font-size:6.5px;font-weight:500;letter-spacing:.3px}
.nav-left{left:119px}.nav-right{left:405px}
.brand{position:absolute;left:258px;top:13px;display:flex;align-items:center;gap:5px;font-weight:700;font-size:14px;color:var(--red);letter-spacing:.3px}
.brand-mark{width:12px;height:12px;background:var(--red);border-radius:2px}
.header-cta{position:absolute;left:531px;top:12px;width:70px;height:20px;background:var(--red);color:#fff;font-size:5.5px;font-weight:600;text-align:center;line-height:7px;padding-top:3px}

/* hero */
.hero{height:338px;overflow:hidden}
.hero-photo{inset:0;background:linear-gradient(180deg,#8c8e92 0%,#b9babd 45%,#d4d5d7 70%,#a9aaad 100%)}
.hero-band{left:269px;top:0;width:80px;height:338px;background:linear-gradient(180deg,#f0403b,#c81c18)}
.hero-title{position:absolute;top:100px;width:100%;text-align:center;color:#fff;font-weight:700;font-size:23px;letter-spacing:1.5px;text-shadow:0 1px 4px rgba(0,0,0,.3)}
.hero-sub{position:absolute;top:132px;width:100%;text-align:center;color:#fff;font-size:9px;line-height:12px;text-shadow:0 1px 3px rgba(0,0,0,.35)}
.btn-outline{position:absolute;left:276px;top:164px;width:68px;height:16px;border:1px solid #fff;background:var(--red);color:#fff;font-size:6px;font-weight:600;text-align:center;line-height:14px}
.chevron{position:absolute;left:302px;top:312px}

.schedule-bar{height:53px;background:var(--navy);display:flex;align-items:center;justify-content:center;gap:26px;color:#fff;font-size:8px}
.btn-red{background:var(--red);color:#fff;font-weight:500;display:inline-flex;align-items:center;justify-content:center;gap:5px}
.schedule-bar .btn-red{width:80px;height:20px;font-size:7.5px}

.section-title{position:absolute;width:100%;text-align:center;font-weight:500;font-size:20px}
.section-title::after{content:"";display:block;width:40px;height:2px;background:var(--red);margin:5px auto 0}
.section-sub{position:absolute;width:100%;text-align:center;font-size:8.5px;line-height:14px;color:#333}

/* projects */
.projects{height:411px}
.filters{left:74px;top:90px;display:flex;gap:8px;font-size:10px}
.filters .active{border-bottom:1.5px solid var(--red)}
.tile{position:absolute}
.tile-caption{position:absolute;left:0;right:0;bottom:6px;text-align:center;font-size:5px;color:#fff}

/* dark bands */
.dark-band{background:var(--dark);overflow:hidden}
.dark-band svg.edges{position:absolute;left:0;top:0}
.design3d{height:298px}
.design3d h2{position:absolute;left:53px;top:68px;color:#fff;font-weight:500;font-size:19px;line-height:22px}
.design3d p{position:absolute;left:53px;top:122px;width:260px;color:#fff;font-size:8.5px;line-height:11px}
.checks{list-style:none}
.checks li{display:flex;align-items:center;gap:3px}
.checks li::before{content:"";width:4px;height:2.5px;border-left:1.2px solid currentColor;border-bottom:1.2px solid currentColor;transform:rotate(-45deg) translateY(-1px);flex:none}
.design3d .checks{position:absolute;left:53px;top:163px;color:#fff;font-size:5.5px;line-height:13px}
.render-ph{background:linear-gradient(160deg,#9a9ca0 0%,#5d5f64 55%,#2e2f33 100%)}
.render-ph.light{background:linear-gradient(160deg,#e4e5e7 0%,#b3b5b9 60%,#85878b 100%)}

/* process */
.process{height:467px;background:var(--light)}
.process-card{position:absolute;top:131px;width:227px;height:308px;padding:15px 18px}
.process-card.light{left:66px;background:#fff;box-shadow:0 1px 6px rgba(0,0,0,.1)}
.process-card.navy{left:328px;background:var(--navy);color:#fff}
.step{position:relative;height:98px}
.step h4{font-size:8.5px;font-weight:600;color:var(--red)}
.navy .step h4{color:#fff}
.step .dur{font-size:7px;font-weight:500}
.step .checks{font-size:6.5px;line-height:10px;margin-top:4px;color:#555}
.step .checks li::before{color:#4caf50}
.navy .step .checks{color:#fff}
.navy .step .checks li::before{color:#fff}
.step .num{position:absolute;right:0;top:14px;font-size:26px;font-weight:600;color:#d4d4d8}
.navy .step .num{color:#fff}

/* materials */
.materials{height:342px}
.mat-card{position:absolute;width:84px;height:93px;background:#fff;box-shadow:0 1px 6px rgba(0,0,0,.12);padding:7px 8px;text-align:center}
.mat-icon{width:18px;height:18px;background:var(--navy);margin:0 auto 4px;display:flex;align-items:center;justify-content:center}
.mat-card h4{font-size:7.5px;font-weight:500}
.mat-card h4::after{content:"";display:block;width:14px;height:1px;background:var(--red);margin:2px auto 3px}
.mat-card .checks{font-size:5px;line-height:8px;text-align:left;padding-left:6px;color:#444}
.mat-card .checks li::before{color:#4caf50}

.consult{height:186px}
.consult h2{position:absolute;left:60px;top:48px;color:#fff;font-weight:500;font-size:20px;line-height:23px}
.consult .btn-red{position:absolute;left:60px;top:124px;width:100px;height:17px;font-size:6.5px}

/* appointment */
.appointment{height:310px}
.tabs{position:absolute;left:44px;top:37px;width:269px;height:20px;display:flex;font-size:6px}
.tabs span{flex:1;display:flex;align-items:center;justify-content:center;border-bottom:1px solid var(--line)}
.tabs .on{background:var(--navy);color:#fff}
.appt-card{position:absolute;left:44px;top:57px;width:269px;height:241px;border:1px solid var(--line);border-top:0;padding:10px 14px;font-size:5px;line-height:7px;color:#666}
.appt-card h5{font-size:6px;font-weight:600;color:var(--ink);margin-top:9px}
.appt-card .opt{border-bottom:1px solid var(--line);padding-bottom:6px}
.appt-steps{position:absolute;left:352px;width:220px}
.appt-steps h4{font-size:9px;font-weight:600;color:var(--navy);line-height:12px}
.appt-steps h4::after{content:"";display:block;width:26px;height:1.5px;background:var(--red);margin:3px 0 4px}
.appt-steps p{font-size:5px;line-height:7px;color:#666}

/* pricing */
.pricing{height:336px;background:var(--light)}
.price-card{position:absolute;top:111px;width:120px;height:199px;background:#fff;box-shadow:0 1px 6px rgba(0,0,0,.1);border-bottom:5px solid var(--navy);text-align:center;padding:13px 12px}
.price-card.featured{border-bottom-color:var(--red)}
.price-card h4{font-size:9px;font-weight:500}
.price-card .lead{font-size:5.5px;line-height:7px;color:#666;margin-top:6px}
.price-card .amount{font-size:12px;font-weight:700;margin:5px 0 8px}
.price-card ul{list-style:none;text-align:left;font-size:5px;line-height:7px;color:#555}
.price-card li{margin-bottom:5px;padding-left:6px;position:relative}
.price-card li::before{content:"";position:absolute;left:0;top:2.5px;width:2.5px;height:2.5px;border-radius:50%;background:var(--ink)}

/* articles */
.articles{height:363px}
.article{position:absolute;overflow:hidden}
.article-caption{position:absolute;left:0;right:0;bottom:0;padding:6px 10px;text-align:center;color:#fff;font-size:7px;line-height:9px;background:linear-gradient(180deg,rgba(0,0,0,0),rgba(0,0,0,.6))}
.show-more{position:absolute;left:271px;top:310px;width:78px;height:22px;font-size:8px}
.divider{position:absolute;left:88px;top:352px;width:444px;height:1px;background:#cfcfd3}

/* faq */
.faq{height:266px}
.eyebrow{position:absolute;left:44px;top:40px;font-size:7px;color:var(--red);font-weight:500}
.faq h2{position:absolute;left:44px;top:55px;font-size:17px;font-weight:600;line-height:20px}
.faq h2::after{content:"";display:block;width:40px;height:2px;background:var(--red);margin-top:3px}
.faq-item{position:absolute;left:44px;width:278px;display:flex;justify-content:space-between;font-size:6.5px;border-bottom:1px solid var(--line);padding-bottom:5px}
.faq-q{position:absolute;left:369px;top:27px;width:28px;height:29px;background:var(--navy);color:#fff;font-size:16px;font-weight:600;text-align:center;line-height:29px}

/* other questions */
.contact-band{height:128px;background:#17181b}
.contact-band h2{position:absolute;left:334px;top:22px;color:#fff;font-weight:500;font-size:20px}
.contact-row{position:absolute;left:334px;display:flex;gap:18px;color:#fff;font-size:8px}

/* footer */
.site-footer{height:165px}
.footer-brand{position:absolute;left:48px;top:42px;display:flex;align-items:center;gap:5px;color:var(--red);font-weight:700;font-size:14px}
.socials{position:absolute;left:60px;top:82px;display:flex;gap:3px}
.socials span{width:14px;height:14px;background:var(--navy)}
.f-col{position:absolute;top:34px}
.f-col h5{font-size:7.5px;font-weight:600;color:var(--navy)}
.f-col h5::after{content:"";display:block;width:16px;height:1.5px;background:var(--red);margin:2px 0 5px}
.f-col ul{list-style:none;font-size:5.5px;line-height:8.5px;color:#444}
.f-btn{display:block;width:78px;height:15px;font-size:5.5px;color:#fff;font-weight:600;text-align:center;line-height:15px;margin-bottom:12px}
.copyright{height:18px;background:var(--dark);color:#fff;font-size:5px;text-align:center;line-height:18px}
</style>
</head>
<body>
<div class="page">

<header class="site-header">
  <nav class="nav nav-left"><span>HOME</span><span>SERVICES</span><span>GALLERY</span></nav>
  <div class="brand"><span class="brand-mark"></span>PLUMVANTA</div>
  <nav class="nav nav-right"><span>BLOG</span><span>ABOUT</span><span>CONTACT</span></nav>
  <div class="header-cta">GET AN ESTIMATE<br>555-014-2290</div>
</header>

<section class="hero">
  <div class="placeholder hero-photo" role="img" aria-label="Photo of a bright grey bathroom with a freestanding tub, plants and wall-hung fixtures"></div>
  <div class="abs hero-band"></div>
  <h1 class="hero-title">BATHROOM REMODELING</h1>
  <p class="hero-sub">It's where you start and end your day. A bathroom remodel<br>will make sure it starts and ends right.</p>
  <span class="btn-outline">BOOK NOW</span>
  <svg class="chevron" width="16" height="14" viewBox="0 0 16 14" fill="none" stroke="#fff" stroke-width="1.3"><path d="M3 2l5 4 5-4M3 7l5 4 5-4"/></svg>
</section>

<div class="schedule-bar">
  <span>Schedule a free in home consultation via our online appointment scheduling system</span>
  <span class="btn-red"><svg width="8" height="8" viewBox="0 0 8 8" fill="none" stroke="#fff" stroke-width=".8"><rect x=".5" y="1.2" width="7" height="6.3"/><path d="M.5 3h7M2.3 0v2M5.7 0v2"/></svg>Schedule</span>
</div>

<section class="projects">
  <h2 class="section-title" style="top:34px">Our Project</h2>
  <div class="abs filters"><span>All</span><span>Room</span><span class="active">Bathroom</span></div>
  <div class="tile" style="left:74px;top:113px;width:230px;height:103px;background:linear-gradient(135deg,#e6e8ea,#b7bcc1)" role="img" aria-label="Bright bathroom with glass shower and wooden vanity"></div>
  <div class="tile" style="left:317px;top:113px;width:108px;height:149px;background:linear-gradient(180deg,#5c5f63,#c9cacb)" role="img" aria-label="Dark bathroom with freestanding tub"></div>
  <div class="tile" style="left:437px;top:113px;width:110px;height:149px;background:linear-gradient(180deg,#3a3c40,#85878a)" role="img" aria-label="Dark tiled shower room"></div>
  <div class="tile" style="left:74px;top:228px;width:108px;height:149px;background:linear-gradient(180deg,#eef0f1,#8d9094)" role="img" aria-label="White bathroom with dark floor and shower door"></div>
  <div class="tile" style="left:194px;top:228px;width:110px;height:149px;background:linear-gradient(180deg,#f3f3f4,#b04a40)" role="img" aria-label="Luxury white bathroom with red rug"><span class="tile-caption">Luxury White Bathroom</span></div>
  <div class="tile" style="left:317px;top:274px;width:230px;height:103px;background:linear-gradient(135deg,#efe9df,#b8aa96)" role="img" aria-label="Marble bathroom with freestanding tub"></div>
</section>

<section class="dark-band design3d">
  <svg class="edges" width="620" height="298" viewBox="0 0 620 298">
    <polygon points="0,0 620,0 620,0 250,14 0,14" fill="#fff"/>
    <polygon points="250,14 620,0 620,18" fill="#d8231f"/>
    <polygon points="0,280 390,284 0,298" fill="#d8231f"/>
    <polygon points="390,284 620,284 620,298 0,298" fill="#fff"/>
  </svg>
  <h2>Bathroom Remodel<br>3D Design</h2>
  <p>Visualize your next remodel before the project begins and gain comfort in knowing you've made the right choices</p>
  <ul class="checks">
    <li>See the finished product before the project starts</li>
    <li>Limit the need for change orders</li>
    <li>Ensure the finished product will be exactly what you want</li>
  </ul>
  <div class="placeholder render-ph" style="left:360px;top:35px;width:200px;height:230px" role="img" aria-label="3D rendered illustration of a bathroom seen through a window"></div>
</section>

<section class="process">
  <h2 class="section-title" style="top:34px">Bathroom Remodeling Process</h2>
  <p class="section-sub" style="top:78px">Our bathroom remodeling process will help you understand the steps it<br>takes to complete your project with associated timelines.</p>
  <div class="process-card light">
    <div class="step"><h4>Initial Consultation</h4><div class="dur">1 hour</div>
      <ul class="checks"><li>Discuss Vision / Goals</li><li>Discuss Budget</li><li>Discuss Materials</li><li>Obtain Measurements</li></ul><span class="num">01</span></div>
    <div class="step"><h4>Draft Proposal</h4><div class="dur">48 hours</div>
      <ul class="checks"><li>Gather Material Pricing</li><li>Gather Labor Pricing</li><li>Detailed Line Item Proposal</li></ul><span class="num">02</span></div>
    <div class="step"><h4>Design</h4><div class="dur">2–4 weeks</div>
      <ul class="checks"><li>Shop for Materials</li><li>Create 3D Design</li><li>Modifications to 3D design</li></ul><span class="num">03</span></div>
  </div>
  <div class="process-card navy">
    <div class="step"><h4>Finalize Proposal</h4><div class="dur">1 week</div>
      <ul class="checks"><li>Finalize Material Cost</li><li>Finalize Labor Cost</li><li>Create Final Proposal</li><li>Proposal Sign Off</li></ul><span class="num">04</span></div>
    <div class="step"><h4>Timeline Varies: 1–6 Weeks</h4>
      <ul class="checks"><li>Demo</li><li>Rough Ins</li><li>Tile &amp; Flooring</li><li>Finishes</li></ul><span class="num">05</span></div>
    <div class="step"><h4>Final Walkthrough</h4><div class="dur">1 hour</div>
      <ul class="checks"><li>Review Project</li><li>Professional Photos</li><li>Enjoy!</li></ul><span class="num">06</span></div>
  </div>
</section>

<section class="materials">
  <h2 class="section-title" style="top:26px">Material Selection</h2>
  <p class="section-sub" style="top:66px">For your bathroom remodel there will be material selections you will have to make.<br>Use the lists below to get an idea of some of the options.</p>
  <div class="placeholder render-ph light" style="left:70px;top:120px;width:210px;height:195px" role="img" aria-label="Silver 3D illustration with a bathroom window"></div>
  <div class="mat-card" style="left:361px;top:121px"><div class="mat-icon"><svg width="9" height="11" viewBox="0 0 9 11"><path d="M5 0L0 6h3.5L3 11 9 4.5H5.5z" fill="#fff"/></svg></div><h4>Electrical</h4><ul class="checks"><li>Light Fixtures</li><li>Heated Floor</li><li>Outlets</li></ul></div>
  <div class="mat-card" style="left:464px;top:121px"><div class="mat-icon"><svg width="11" height="9" viewBox="0 0 11 9" fill="none" stroke="#fff" stroke-width="1"><path d="M1 4h9v2a2 2 0 01-2 2H3a2 2 0 01-2-2z M2 4V1.5a1 1 0 012 0"/></svg></div><h4>Plumbing</h4><ul class="checks"><li>Vanity Fixtures</li><li>Shower Fixtures</li><li>Toilet</li></ul></div>
  <div class="mat-card" style="left:361px;top:223px"><div class="mat-icon"><svg width="10" height="10" viewBox="0 0 10 10" fill="none" stroke="#fff" stroke-width="1"><path d="M1 9l5-5M6 1l3 3-2 2-3-3z"/></svg></div><h4>Tile &amp; Flooring</h4><ul class="checks"><li>Shower Wall Tile</li><li>Shower Floor Tile</li><li>Bathroom Flooring</li></ul></div>
  <div class="mat-card" style="left:464px;top:223px"><div class="mat-icon"><svg width="10" height="10" viewBox="0 0 10 10" fill="none" stroke="#fff" stroke-width="1"><rect x="1" y="1" width="3.5" height="3.5"/><rect x="5.5" y="1" width="3.5" height="3.5"/><rect x="1" y="5.5" width="3.5" height="3.5"/><rect x="5.5" y="5.5" width="3.5" height="3.5"/></svg></div><h4>Finishes</h4><ul class="checks"><li>Trim</li><li>Mirrors &amp; Towel Bars</li><li>Cabinetry &amp; Counter Tops</li></ul></div>
</section>

<section class="dark-band consult">
  <svg class="edges" width="620" height="186" viewBox="0 0 620 186">
    <polygon points="0,0 620,0 620,12 0,0" fill="#fff"/>
    <polygon points="0,0 330,10 0,16" fill="#d8231f"/>
    <polygon points="0,0 620,0 620,14 330,10" fill="#fff"/>
    <polygon points="260,176 620,168 620,186" fill="#d8231f"/>
  </svg>
  <h2>Schedule Your Free<br>Consultation Today!</h2>
  <span class="btn-red">Schedule Below
    <svg width="6" height="7" viewBox="0 0 6 7" fill="none" stroke="#fff" stroke-width="1"><path d="M3 0v6M.5 3.5L3 6l2.5-2.5"/></svg></span>
  <div class="placeholder render-ph" style="left:411px;top:27px;width:168px;height:141px" role="img" aria-label="Silver 3D illustration over a dark bathroom scene"></div>
</section>

<section class="appointment">
  <div class="tabs"><span class="on">Choose Appointment</span><span>Your Info</span><span>Confirmation</span></div>
  <div class="appt-card">
    <p class="opt">This is the time that works best for your schedule. If you cannot find a time that works for you, please contact us. We will be flexible on finding a time that fits.</p>
    <h5>Estimate</h5>
    <p class="opt">If you are ready for us to visit, one of our team will meet you at your home to discuss the project and take measurements for your proposal.</p>
    <h5>Conference Call</h5>
    <p class="opt">Just want to chat about a potential project? Schedule a time and one of our experts will call to discuss your project.</p>
    <h5>Virtual Appointment (Video Meeting)</h5>
    <p class="opt">We offer video meetings for clients who prefer to meet online. You can share your space and give us a rough estimate before we visit in person.</p>
  </div>
  <div class="appt-steps" style="top:48px"><h4>1. Schedule an Appointment Today</h4><p>View our calendar on the left and pick an appointment time that works best for you.</p></div>
  <div class="appt-steps" style="top:96px"><h4>2. Review our "Things to Think About<br>Checklist"</h4><p>There are a lot of things that go into a remodel. To prepare for our visit, review the checklist so that your answers are ready. This will help us prepare a proposal for you.</p></div>
  <div class="appt-steps" style="top:184px"><h4>3. Appointment</h4><p>One of our project managers will meet with you to discuss the project, take measurements and listen to your vision for the space.</p></div>
</section>

<section class="pricing">
  <h2 class="section-title" style="top:22px">Pricing Packages</h2>
  <p class="section-sub" style="top:66px">Pricing Basement Finishes can vary dramatically, below you will find<br>typical services with the varying coost Level</p>
  <div class="price-card" style="left:108px"><h4>Minor Finish</h4><p class="lead">Lorem ipsum dolor sit amet, consectetur adipiscing</p><div class="amount">19$</div>
    <ul><li>Small copy of certificate of incorporation</li><li>Small copy of memorandum &amp; articles of association</li><li>Must explain to you how all this mistaken idea</li><li>Small copy of company register with first entrie</li></ul></div>
  <div class="price-card featured" style="left:250px"><h4>Moderate Finish</h4><p class="lead">Lorem ipsum dolor sit amet, consectetur adipiscing</p><div class="amount">19$</div>
    <ul><li>Small copy of certificate of incorporation</li><li>Small copy of memorandum &amp; articles of association</li><li>Small copy of share certificate</li><li>Small copy of company register with first entrie</li></ul></div>
  <div class="price-card" style="left:392px"><h4>Major Finish</h4><p class="lead">Lorem ipsum dolor sit amet, consectetur adipiscing</p><div class="amount">19$</div>
    <ul><li>Small copy of certificate of incorporation</li><li>Small copy of memorandum &amp; articles of association</li><li>Small copy of share certificate</li><li>Small copy of company register with first entrie</li></ul></div>
</section>

<section class="articles">
  <h2 class="section-title" style="top:30px">Helpful Articles</h2>
  <div class="article" style="left:74px;top:92px;width:234px;height:193px;background:linear-gradient(180deg,#9fb6cc,#8a6d4c 60%,#4a3a2a)" role="img" aria-label="House under construction with timber frame"><div class="article-caption">Home Remodeling Made Easier with Simple</div></div>
  <div class="article" style="left:320px;top:92px;width:225px;height:93px;background:linear-gradient(135deg,#c6c9cc,#7b6f66)" role="img" aria-label="Worker using a power tool"><div class="article-caption">Handyman vs. Contractor – Who Should<br>You Call?</div></div>
  <div class="article" style="left:320px;top:191px;width:225px;height:94px;background:linear-gradient(135deg,#8d2a24,#d8d2c8)" role="img" aria-label="Tools and renovation plans on a table"><div class="article-caption">Keeping Costs Reasonable When Planning<br>Whole Home Remodeling</div></div>
  <span class="btn-red show-more">Show More</span>
  <div class="divider"></div>
</section>

<section class="faq">
  <span class="eyebrow">Why Work With Us</span>
  <h2>Frequently Asked<br>Questions</h2>
  <div class="faq-item" style="top:120px"><span>How much does a bathroom remodel cost?</span><span>+</span></div>
  <div class="faq-item" style="top:145px"><span>How long will it take?</span><span>+</span></div>
  <div class="faq-item" style="top:169px"><span>Do you pull permits?</span><span>+</span></div>
  <div class="faq-item" style="top:194px"><span>Are you licensed and insured?</span><span>+</span></div>
  <div class="placeholder" style="left:351px;top:27px;width:223px;height:197px;background:linear-gradient(180deg,#f1f1f2,#d9d4cf)" role="img" aria-label="Thoughtful woman in a beige sweater"></div>
  <div class="faq-q">?</div>
</section>

<section class="contact-band">
  <div class="placeholder render-ph" style="left:101px;top:14px;width:106px;height:100px;opacity:.6" role="img" aria-label="Faint silver 3D decoration"></div>
  <h2>Other Questions?</h2>
  <div class="contact-row" style="top:67px"><span>Contact us at</span><span>555-014-2290</span></div>
  <div class="contact-row" style="top:90px"><span>Reach out to our</span><span>Support Team</span></div>
</section>

<footer class="site-footer">
  <div class="footer-brand"><span class="brand-mark"></span>PLUMVANTA</div>
  <div class="socials"><span></span><span></span><span></span><span></span></div>
  <div class="f-col" style="left:214px"><h5>GET A QUOTE</h5>
    <span class="f-btn" style="background:var(--red)">CONTACT US</span>
    <span class="f-btn" style="background:var(--navy)">GET STARTED</span></div>
  <div class="f-col" style="left:358px"><h5>SERVICES</h5>
    <ul><li>Basement Finishing</li><li>Bathroom Remodeling</li><li>Handyman</li><li>Kitchen Remodeling</li><li>Window Replacement</li><li>Whole Home</li><li>Remodeling</li></ul></div>
  <div class="f-col" style="left:491px"><h5>SERVICE AREAS</h5>
    <ul><li>Ashfield, ST</li><li>Corvale, ST</li><li>Linmoor, ST</li><li>Pell Ridge, ST</li><li>Oakhurst, ST</li><li>Halden, ST</li><li>Westmere, ST</li><li>View All</li></ul></div>
</footer>
<div class="copyright">Copyright ©2021 Plumvanta. All Rights Reserved</div>

</div>
</body>
</html>
```